Name Card Design

Looking to create a card for my business. I am a personal stylist, my business is clothes, shoes and everything to do with looking fashion forward. I help people achieve the most polished look with cloths and grooming. I would like my card to be a reflection of my qualities which are: poise, elegance, creativity and fairness.
Things I like a simple yet expensive looking, sometimes less simple but highly creative and different catches my eye. For instance I saw a card with lace trimming at the bottom, it made me think about the business that person was in. I don't like childish designs with butterflies, trees, flowers, etc.
Here is my site www.Marta-Venn.example for your perusal

On the card it should have the following info
Marta Venn
personal stylist
www.Marta-Venn.example
(+65) 842-30587
Facebook page: Ringtochic

Back of the card:
Wardrobe weeding
Personal shopping
Style consultation

Target Market(s)

mostly working women

Industry/Entity Type

Fashion

Font styles to use
Serif
Sans Serif

Requirements
Should not have
• butterflies, flowers, feathers, etc

```html
<!DOCTYPE html>
<html lang="en">
<head>
<meta charset="utf-8">
<title>Marta Venn – Personal Stylist Card</title>
<link rel="stylesheet" href="https://fonts.googleapis.com/css2?family=Alegreya:wght@700&family=Alegreya+Sans:wght@400&family=Parisienne&family=PT+Sans&display=swap">
<style>
  :root {
    --backdrop: #e9ecef;
    --card-white: #ffffff;
    --sky: #4cc5e3;
    --teal: #14708f;
    --ink: #2b2b2b;
    --contact: #ffffff;
  }
  html, body {
    margin: 0;
    width: 1200px;
    height: 767px;
    overflow: hidden;
    background: var(--backdrop);
  }
  .canvas {
    position: relative;
    width: 1200px;
    height: 767px;
  }
  .card {
    position: absolute;
    left: 85px;
    top: 88px;
    width: 1030px;
    height: 592px;
    border-radius: 40px;
    background: var(--card-white);
    overflow: hidden;
  }
  .card-waves {
    position: absolute;
    inset: 0;
  }
  .brand-name {
    position: absolute;
    left: 50px;
    top: 66px;
    margin: 0;
    font-family: "Alegreya", Georgia, serif;
    font-weight: 700;
    font-size: 104px;
    line-height: 1;
    color: var(--sky);
    letter-spacing: 0.5px;
  }
  .brand-role {
    position: absolute;
    left: 260px;
    top: 182px;
    margin: 0;
    font-family: "Alegreya", Georgia, serif;
    font-weight: 700;
    font-size: 36px;
    line-height: 1;
    color: var(--teal);
  }
  .services {
    position: absolute;
    left: 20px;
    top: 308px;
    width: 640px;
    margin: 0;
    padding: 0;
    list-style: none;
    font-family: "Parisienne", cursive;
    font-size: 33px;
    color: var(--ink);
    line-height: 48px;
  }
  .services li {
    display: inline-flex;
    align-items: center;
    margin-right: 12px;
  }
  .service-icon {
    width: 26px;
    height: 26px;
    margin-right: 6px;
    fill: none;
    stroke: var(--ink);
    stroke-width: 1.6;
  }
  .contact {
    position: absolute;
    right: 40px;
    top: 412px;
    margin: 0;
    padding: 0;
    list-style: none;
    text-align: right;
    font-family: "PT Sans", "Alegreya Sans", Arial, sans-serif;
    font-size: 28px;
    line-height: 40px;
    color: var(--contact);
  }
  .contact li {
    display: flex;
    justify-content: flex-end;
    align-items: center;
  }
  .contact-icon {
    width: 22px;
    height: 22px;
    margin-right: 7px;
    fill: none;
    stroke: var(--contact);
    stroke-width: 1.6;
  }
  .contact-dot {
    width: 20px;
    height: 20px;
    margin-right: 7px;
    border-radius: 50%;
    background: var(--contact);
  }
</style>
</head>
<body>
<div class="canvas">
  <section class="card" aria-label="Business card">
    <svg class="card-waves" width="1030" height="592" viewBox="0 0 1030 592" aria-hidden="true">
      <path fill="var(--sky)" d="M1030,20 C930,170 800,320 560,440 C420,505 220,520 0,497 L0,592 L1030,592 Z"/>
      <path fill="var(--teal)" d="M0,448 C200,530 470,470 722,326 C480,490 240,540 0,492 Z"/>
    </svg>

    <h1 class="brand-name">MartaVenn</h1>
    <p class="brand-role">Personal Stylist</p>

    <ul class="services">
      <li>
        <svg class="service-icon" viewBox="0 0 26 26"><circle cx="13" cy="16" r="7"/><path d="M10,6 L13,3 L16,6 L13,9 Z"/></svg>
        Wardrobe Weeding
      </li>
      <li>
        <svg class="service-icon" viewBox="0 0 26 26"><path d="M2,5 H6 L9,17 H21 L23,8 H7"/><circle cx="11" cy="21" r="2"/><circle cx="19" cy="21" r="2"/></svg>
        Personal Shopping
      </li>
      <li>
        <svg class="service-icon" viewBox="0 0 26 26"><ellipse cx="10" cy="11" rx="8" ry="6"/><ellipse cx="16" cy="15" rx="8" ry="6"/></svg>
        Style consultation
      </li>
    </ul>

    <ul class="contact">
      <li>
        <svg class="contact-icon" viewBox="0 0 22 22"><circle cx="11" cy="11" r="9.5"/><path d="M8,6 C6,9 8,15 13,16 L15,14 L13,12 L12,13 C10,12 9.5,10.5 10,9 L11,8 L9,6 Z"/></svg>
        (+65) 842-30587
      </li>
      <li>
        <svg class="contact-icon" viewBox="0 0 22 22"><circle cx="11" cy="11" r="9.5"/><ellipse cx="11" cy="11" rx="4" ry="9.5"/><path d="M1.5,11 H20.5 M3.5,6 H18.5 M3.5,16 H18.5"/></svg>
        www.Marta-Venn.example
      </li>
      <li>
        <span class="contact-dot" aria-hidden="true"></span>
        Ringtochic
      </li>
    </ul>
  </section>
</div>
</body>
</html>
```